Business Card, Stationary Folder & Envelope
ORVALUX
Creative Brief
Bright & Fun-filled
Ramiro Quesada
TRL
Carretera Pueblanco - Ozumel Km 3.4, Colonia El Prado Tepalcingo, P.C. 90487, Tlaxcala, Tlax., México
VOXEL ID 57*83*40962
ramiro.quesada@orvalux.example
www.orvalux.example

```html
<!DOCTYPE html>
<html lang="es">
<head>
<meta charset="utf-8">
<title>ORVALUX – Tarjetas de presentación</title>
<link rel="stylesheet" href="https://fonts.googleapis.com/css2?family=Open+Sans:ital,wght@0,400;0,700;0,800;1,700&display=swap">
<style>
  :root {
    --bg: #e9e6e1;
    --card-white: #ffffff;
    --navy-deep: #04101c;
    --navy: #0b2a44;
    --cyan-glow: #2a8fc4;
    --swoosh: #9a9ea3;
    --logo-grey: #4a4f55;
    --text-light: #ffffff;
    --text-soft: #d5e6f2;
  }
  * { margin: 0; padding: 0; box-sizing: border-box; }
  html, body { width: 1200px; height: 852px; overflow: hidden; }
  body { background: var(--bg); font-family: "Open Sans", Arial, sans-serif; position: relative; }

  .card {
    position: absolute;
    width: 520px; height: 300px;
    background: var(--card-white);
    border-radius: 16px;
    overflow: hidden;
    box-shadow: 0 6px 18px rgba(0,0,0,.18);
  }
  .card--contact-left { left: 70px; top: 140px; }
  .card--contact-right { left: 610px; top: 412px; }

  .card__art { position: absolute; inset: 0; width: 100%; height: 100%; }

  .brand {
    position: absolute;
    display: flex; align-items: center; gap: 9px;
    font-weight: 800; font-size: 26px; letter-spacing: 1px;
    line-height: 1;
    color: var(--logo-grey);
    white-space: nowrap;
  }
  .brand__dot { width: 24px; height: 24px; border-radius: 50%; background: var(--cyan-glow); flex: none; }
  .card--contact-left .brand { left: 318px; top: 132px; }
  .card--contact-right .brand { left: 22px; top: 110px; }

  .holder { position: absolute; color: var(--text-light); }
  .holder__name { font-weight: 700; font-style: italic; font-size: 15px; }
  .holder__title { font-weight: 700; font-size: 10px; margin-top: 2px; }
  .card--contact-left .holder { left: 18px; top: 30px; }
  .card--contact-right .holder { right: 24px; top: 56px; text-align: right; }

  .address, .contacts { position: absolute; color: var(--text-soft); font-size: 10.5px; line-height: 1.5; }
  .card--contact-left .address { left: 18px; top: 100px; }
  .card--contact-left .contacts { left: 18px; top: 162px; }
  .card--contact-right .address { right: 24px; top: 100px; text-align: right; }
  .card--contact-right .contacts { right: 24px; top: 160px; text-align: right; }

  .contacts__row { display: flex; align-items: center; gap: 7px; height: 16px; white-space: nowrap; }
  .card--contact-right .contacts__row { justify-content: flex-end; }
  .contacts__row--plain { padding-left: 19px; }
  .card--contact-right .contacts__row--plain { padding-left: 0; padding-right: 19px; }
  .contacts__gap { height: 8px; }
  .icon { width: 12px; height: 12px; flex: none; }
</style>
</head>
<body>

<!-- Card A: contact panel on the left, brand on the right -->
<article class="card card--contact-left">
  <svg class="card__art" viewBox="0 0 520 300" aria-hidden="true">
    <defs>
      <radialGradient id="glowA" cx="0.35" cy="0.62" r="0.7">
        <stop offset="0" stop-color="#2a8fc4"/>
        <stop offset="0.45" stop-color="#0b2a44"/>
        <stop offset="1" stop-color="#04101c"/>
      </radialGradient>
    </defs>
    <path d="M0,0 H305 C235,95 330,215 215,300 H0 Z" fill="#d9dcdf"/>
    <path d="M0,0 H296 C222,95 318,215 200,300 H0 Z" fill="var(--swoosh)"/>
    <path d="M0,0 H284 C208,95 300,215 184,300 H0 Z" fill="url(#glowA)"/>
  </svg>

  <div class="holder">
    <div class="holder__name">Ramiro Quesada</div>
    <div class="holder__title">TRL</div>
  </div>
  <div class="address">
    Carretera Pueblanco - Ozumel Km 3.4,<br>
    Colonia El Prado Tepalcingo,<br>
    P.C. 90487, Tlaxcala, Tlax., México
  </div>
  <div class="contacts">
    <div class="contacts__row contacts__row--plain">VOXEL ID 57*83*40962</div>
    <div class="contacts__row">
      <svg class="icon" viewBox="0 0 12 12"><path d="M2,1 L4.5,1 L5.3,3.5 L4,4.6 C4.8,6.3 5.7,7.2 7.4,8 L8.5,6.7 L11,7.5 L11,10 C6,10.5 1.5,6 2,1 Z" fill="#fff"/></svg>
      +52 (246) 555-0142
    </div>
    <div class="contacts__row">
      <svg class="icon" viewBox="0 0 12 12"><rect x="3.5" y="0.5" width="5" height="11" rx="1" fill="#fff"/><rect x="4.5" y="2" width="3" height="6" fill="#0b2a44"/></svg>
      +52 (222) 555 01 87
    </div>
    <div class="contacts__row">
      <svg class="icon" viewBox="0 0 12 12"><rect x="1" y="4" width="10" height="7" rx="1" fill="#fff"/><rect x="3" y="1" width="6" height="4" fill="#fff"/></svg>
      +52 (246) 555-0163
    </div>
    <div class="contacts__gap"></div>
    <div class="contacts__row">
      <svg class="icon" viewBox="0 0 12 12"><rect x="0.5" y="2.5" width="11" height="7" fill="#fff"/><path d="M0.5,2.5 L6,7 L11.5,2.5" fill="none" stroke="#0b2a44" stroke-width="1"/></svg>
      ramiro.quesada@orvalux.example
    </div>
    <div class="contacts__row">
      <svg class="icon" viewBox="0 0 12 12"><circle cx="6" cy="6" r="5" fill="none" stroke="#fff" stroke-width="1.2"/><path d="M1,6 H11 M6,1 C3,4 3,8 6,11 M6,1 C9,4 9,8 6,11" fill="none" stroke="#fff" stroke-width="0.9"/></svg>
      www.orvalux.example
    </div>
  </div>

  <div class="brand"><span class="brand__dot"></span>ORVALUX</div>
</article>

<!-- Card B: brand on the left, contact panel on the right -->
<article class="card card--contact-right">
  <svg class="card__art" viewBox="0 0 520 300" aria-hidden="true">
    <defs>
      <radialGradient id="glowB" cx="0.38" cy="0.95" r="0.72">
        <stop offset="0" stop-color="#2a8fc4"/>
        <stop offset="0.45" stop-color="#0b2a44"/>
        <stop offset="1" stop-color="#04101c"/>
      </radialGradient>
    </defs>
    <path d="M262,0 H520 V300 H110 C230,235 200,95 262,0 Z" fill="#d9dcdf"/>
    <path d="M272,0 H520 V300 H122 C242,235 210,95 272,0 Z" fill="var(--swoosh)"/>
    <path d="M284,0 H520 V300 H136 C256,235 222,95 284,0 Z" fill="url(#glowB)"/>
  </svg>

  <div class="brand"><span class="brand__dot"></span>ORVALUX</div>

  <div class="holder">
    <div class="holder__name">Ramiro Quesada</div>
    <div class="holder__title">TRL</div>
  </div>
  <div class="address">
    Carretera Pueblanco - Ozumel Km 3.4,<br>
    Colonia El Prado Tepalcingo,<br>
    P.C. 90487, Tlaxcala, Tlax., México
  </div>
  <div class="contacts">
    <div class="contacts__row contacts__row--plain">VOXEL ID 57*83*40962</div>
    <div class="contacts__row">
      +52 (246) 555-0142
      <svg class="icon" viewBox="0 0 12 12"><path d="M2,1 L4.5,1 L5.3,3.5 L4,4.6 C4.8,6.3 5.7,7.2 7.4,8 L8.5,6.7 L11,7.5 L11,10 C6,10.5 1.5,6 2,1 Z" fill="#fff"/></svg>
    </div>
    <div class="contacts__row">
      +52 (222) 555 01 87
      <svg class="icon" viewBox="0 0 12 12"><rect x="3.5" y="0.5" width="5" height="11" rx="1" fill="#fff"/><rect x="4.5" y="2" width="3" height="6" fill="#0b2a44"/></svg>
    </div>
    <div class="contacts__row">
      +52 (246) 555-0163
      <svg class="icon" viewBox="0 0 12 12"><rect x="1" y="4" width="10" height="7" rx="1" fill="#fff"/><rect x="3" y="1" width="6" height="4" fill="#fff"/></svg>
    </div>
    <div class="contacts__gap"></div>
    <div class="contacts__row">
      ramiro.quesada@orvalux.example
      <svg class="icon" viewBox="0 0 12 12"><rect x="0.5" y="2.5" width="11" height="7" fill="#fff"/><path d="M0.5,2.5 L6,7 L11.5,2.5" fill="none" stroke="#0b2a44" stroke-width="1"/></svg>
    </div>
    <div class="contacts__row">
      www.orvalux.example
      <svg class="icon" viewBox="0 0 12 12"><circle cx="6" cy="6" r="5" fill="none" stroke="#fff" stroke-width="1.2"/><path d="M1,6 H11 M6,1 C3,4 3,8 6,11 M6,1 C9,4 9,8 6,11" fill="none" stroke="#fff" stroke-width="0.9"/></svg>
    </div>
  </div>
</article>

</body>
</html>
```